Stationery Design Project

We need a stationery design package for a new company based in Luxembourg called "Morvesta Tax & Consulting" with a legal name "Morvesta S.a.r.l.".

We are a personal tax compliance and consulting company specialising in Luxembourg, UK and US taxation.

We require a stationery package including the following:-

- letterhead/paper
- envelopes (C4, C5, DL)
- compliments slip
- business cards
- folder (A4 with two pockets)

We are looking for a modern, elegant design which remains professional.
Updates

Hi everyone, thank you for the designs so far - there are some that we do like so I have changed the status to non-refundable as we will definitely take one of them forwards.

I have today received the final logo files from the website designer so I will upload these shortly.  We are reviewing the designs to date tonight so will provide further feedback latest tomorrow morning.

Thanks again
Greta

Industry/Entity Type

Business

Requirements
Must have
• The design should focus on the following main colour:-
#7D1935
and could use these two colours as accents, if required:-
#4A96AD
#F5F3EE

We have uploaded our logo which has been finalised 31 July 2013 (note I have deleted the previous logo files that were uploaded). I have uploaded jpg, png, psd files. I also have tif and eps but these are large in size so have not uploaded here - if you need them please let me know and I can upload.
Nice to have
• Business cards - we would like the business cards to be full main colour on one side. We are considering using a QR code on the business card to link to the website, but not a necessity.

Folder - we are considering including the company contact information preprinted on the inside right pocket instead of business cards

```html
<!DOCTYPE html>
<html lang="en">
<head>
<meta charset="utf-8">
<title>Morvesta Tax &amp; Consulting – Business Cards</title>
<link rel="stylesheet" href="https://fonts.googleapis.com/css2?family=Arimo:wght@400;700&display=swap">
<style>
  :root {
    --brand-maroon: #7D1935;
    --accent-teal: #4A96AD;
    --paper: #F5F3EE;
    --ink-grey: #5c5c5c;
    --mark-grey: #8a8a8a;
    --stage: #e4e2de;
  }
  * { box-sizing: border-box; margin: 0; padding: 0; }
  html, body {
    width: 1200px; height: 900px; overflow: hidden;
    background: var(--stage);
    font-family: "Arimo", Arial, sans-serif;
  }
  .card-sheet {
    position: relative; width: 1200px; height: 900px;
    display: flex; align-items: center; justify-content: center; gap: 48px;
  }
  .card {
    position: relative; width: 540px; height: 309px;
    box-shadow: 0 6px 18px rgba(0,0,0,.18);
  }
  .card--front { background: var(--brand-maroon); }
  .card--back { background: var(--paper); }

  .brand {
    position: absolute; display: flex; align-items: center; gap: 16px;
  }
  .brand__dot {
    width: 74px; height: 74px; border-radius: 50%;
    border: 4px solid var(--mark-grey); flex: none;
  }
  .brand__name { font-weight: 400; line-height: 1; }
  .brand__main { display: block; font-size: 40px; letter-spacing: 1px; }
  .brand__sub { display: block; font-size: 15px; letter-spacing: 1.2px; margin-top: 5px; }

  .card--front .brand { left: 120px; top: 150px; }
  .card--front .brand__name { color: #ffffff; }
  .card--front .brand__dot { border-color: #b7b1b3; }

  .card--back .brand { left: 34px; top: 34px; }
  .card--back .brand__name { color: var(--brand-maroon); }

  .person {
    position: absolute; left: 34px; top: 140px; right: 34px;
    display: flex; align-items: baseline; gap: 10px; color: var(--ink-grey);
  }
  .person__name { font-size: 21px; }
  .person__role { font-size: 12px; }

  .rule {
    position: absolute; left: 34px; right: 34px; height: 1px;
    background: var(--accent-teal);
  }
  .rule--top { top: 176px; }
  .rule--bottom { top: 240px; }

  .contacts {
    position: absolute; left: 34px; right: 34px; top: 188px;
    display: grid; grid-template-columns: 1fr 1fr; row-gap: 6px;
    font-size: 13px; color: var(--ink-grey);
  }
  .contacts__label { display: inline-block; width: 18px; }

  .links {
    position: absolute; left: 34px; right: 34px; top: 254px;
    display: grid; grid-template-columns: 1fr 1fr;
    font-size: 13px; color: var(--ink-grey);
  }
  .links__label { color: var(--accent-teal); font-weight: 700; margin-right: 8px; }
  .links__web { color: var(--accent-teal); font-weight: 700; }
</style>
</head>
<body>
<main class="card-sheet">
  <section class="card card--front" aria-label="Business card front">
    <div class="brand">
      <span class="brand__dot"></span>
      <p class="brand__name">
        <span class="brand__main">MORVESTA</span>
        <span class="brand__sub">TAX &amp; CONSULTING</span>
      </p>
    </div>
  </section>

  <section class="card card--back" aria-label="Business card back">
    <div class="brand">
      <span class="brand__dot"></span>
      <p class="brand__name">
        <span class="brand__main">MORVESTA</span>
        <span class="brand__sub">TAX &amp; CONSULTING</span>
      </p>
    </div>

    <div class="person">
      <span class="person__name">Elena Marchetti</span>
      <span class="person__role">Executive Director</span>
    </div>

    <div class="rule rule--top"></div>

    <div class="contacts">
      <span><span class="contacts__label">T</span>+352 26 47 80 112</span>
      <span><span class="contacts__label">M</span>+352 62 19 44 270</span>
      <span><span class="contacts__label">T</span>+352 26 47 80 113</span>
      <span><span class="contacts__label">E</span>info@morvesta-tax.lu</span>
    </div>

    <div class="rule rule--bottom"></div>

    <div class="links">
      <span><span class="links__label">Chat</span>morvesta.tax</span>
      <span class="links__web">www.morvesta-tax.lu</span>
    </div>
  </section>
</main>
</body>
</html>
```